Website Design for PawRank - New Digital Agency

We are creating a new digital marketing agency and need a new website. I have attached the logo. Our niche is going to be veterinarians. Use the same colors as in the logo (blue, white and gray).

I want real pictures of real people in this and not just boring stock photos. It needs to be related to the industry.

Home page (example:https://trellmarsh.com/)
Service page (example: https://dovequist.com/consulting/)
Case study page (example: https://www.harlowfinchley.com/seo/case-study/)

I will continue to update this brief.
Updates

I updated the brief with some additional sample sites 2 days ago and want to see more designs. I won't need that may more days ...just a few more.

Target Market(s)

veterinarians

Font styles to use
Sans Serif

Requirements
Must have
• I want a very clean looking site. Use the same colors as in the logo (blue, white and gray).
Nice to have
• We need to build this with the idea that the purpose is to generate leads for our business.
• Home page (example:https://trellmarsh.com/)
• Service page (example: https://dovequist.com/consulting/)
• Case study page (example: https://www.harlowfinchley.com/seo/case-study/)

```html
<!DOCTYPE html>
<html lang="en">
<head>
<meta charset="utf-8">
<title>PawRank — Free Exclusive Traffic Tips</title>
<link href="https://fonts.googleapis.com/css2?family=Outfit:wght@500;600;700&family=Mulish:wght@400;600;700&display=swap" rel="stylesheet">
<style>
:root{
  --blue:#0d57a7;
  --blue-accent:#2a8fd4;
  --blue-pale:#e4eef8;
  --gray-bg:#f4f5f7;
  --gray-line:#e2e4e8;
  --gray-mark:#cdd0d5;
  --text:#4a4f57;
  --text-soft:#6b7078;
  --white:#ffffff;
}
*{margin:0;padding:0;box-sizing:border-box}
html,body{width:1200px;height:3198px;overflow:hidden}
body{position:relative;background:var(--white);font-family:"Mulish",sans-serif;color:var(--text)}
.abs{position:absolute}

/* hero */
.hero-bg{left:0;top:0;width:1200px;height:760px}
.brand{left:149px;top:36px;font-weight:700;font-size:32px;color:var(--white);letter-spacing:-.5px}
.nav{top:52px;font-weight:700;font-size:12px;color:var(--white)}
.nav-contact{left:959px;top:43px;width:91px;height:31px;border-radius:16px;background:var(--white);color:var(--blue);font-weight:700;font-size:12px;display:flex;align-items:center;justify-content:center}
.hero-title{left:149px;top:222px;font-family:"Outfit",sans-serif;font-weight:600;font-size:57px;line-height:65px;color:var(--white)}
.hero-sub{left:148px;top:362px;font-size:17.5px;line-height:25px;color:var(--white);font-weight:600}
.signup{left:150px;top:452px;width:337px;height:46px;border-radius:23px;background:var(--white);border:3px solid #d9e6f4}
.signup-input{left:22px;top:12px;font-size:10.5px;color:#a4a8ae;display:flex;align-items:center;gap:8px}
.signup-btn{right:2px;top:2px;width:104px;height:36px;border-radius:18px;background:var(--blue);color:var(--white);font-weight:700;font-size:12px;display:flex;align-items:center;justify-content:center}
.hero-photo{left:600px;top:118px;width:450px;height:600px;border-radius:200px 200px 0 0;background:linear-gradient(180deg,#c9b6a6 0%,#7d8188 35%,#5b6068 100%)}

/* news */
.news-label{left:0;width:1200px;top:746px;text-align:center;font-weight:700;font-size:13px;color:var(--blue)}
.news-mark{top:832px;height:24px;border-radius:4px;background:var(--gray-mark)}
.divider{left:149px;width:901px;height:1px;background:var(--gray-line)}

/* testimonials */
.quote-mark{font-family:"Outfit",sans-serif;font-weight:700;font-size:56px;line-height:56px;color:var(--blue)}
.quote-text{font-size:18px;line-height:30px;color:var(--text)}
.quote-by{font-size:13px;color:var(--text-soft)}
.quote-by strong{color:var(--blue);font-weight:700}

/* case study */
.case{left:0;top:1574px;width:1200px;height:1330px;background:var(--gray-bg)}
.case-title{left:0;width:1200px;top:1641px;text-align:center;font-family:"Outfit",sans-serif;font-weight:600;font-size:37px;line-height:42px;color:var(--blue)}
.author{left:0;width:1200px;top:1748px;display:flex;justify-content:center;align-items:center;gap:14px;font-size:13px;color:var(--text-soft)}
.author-pic{width:46px;height:46px;border-radius:50%;background:radial-gradient(circle at 50% 40%,#c8b1a0 0 30%,#5f6670 60%,#eef1f5 62%);border:3px solid var(--white)}
.sub-head{left:263px;font-weight:700;font-size:17px;color:var(--blue)}
.body-copy{left:263px;width:674px;font-size:13.3px;line-height:21px;color:var(--text);text-align:justify}
.chart-card{left:263px;top:2154px;width:674px;height:285px;border-radius:4px;background:linear-gradient(180deg,#f7f8fa 0 30px,#ffffff 30px 45%,#dbeaf7 80%,#ffffff 100%);box-shadow:0 6px 20px rgba(20,40,80,.08)}
.cta{left:480px;top:2626px;width:240px;height:38px;border-radius:19px;background:var(--blue);color:var(--white);font-weight:700;font-size:11.5px;display:flex;align-items:center;justify-content:center}

/* footer */
.footer-bg{left:0;top:2690px;width:1200px;height:508px}
.foot-head{font-weight:700;font-size:14px;color:var(--white)}
.foot-link{font-weight:700;font-size:11.5px;color:var(--white)}
.social{width:23px;height:23px;border-radius:50%;border:1.5px solid var(--white)}
.copyright{left:0;width:1200px;top:3153px;text-align:center;font-size:11px;color:#c9d8ee}
</style>
</head>
<body>

<!-- hero -->
<svg class="abs hero-bg" viewBox="0 0 1200 760" aria-hidden="true">
  <rect width="1200" height="760" fill="#f4f5f7"/>
  <polygon points="0,750 1200,640 1200,760 0,760" fill="#ffffff"/>
  <polygon points="0,0 1200,0 1200,716 0,562" fill="#0d57a7"/>
  <polygon points="990,680 1200,542 1200,748" fill="#2a8fd4"/>
</svg>
<div class="abs hero-photo" role="img" aria-label="Photo of a smiling consultant in a grey suit with arms crossed"></div>

<div class="abs brand">PawRank</div>
<div class="abs nav" style="left:620px">Home</div>
<div class="abs nav" style="left:683px">Company</div>
<div class="abs nav" style="left:765px">Service</div>
<div class="abs nav" style="left:836px">Tools</div>
<div class="abs nav" style="left:897px">Blog</div>
<div class="abs nav-contact">Contact</div>

<h1 class="abs hero-title">Free Exclusive<br>Traffic Tips</h1>
<p class="abs hero-sub">Enter your email below to get access to my proven<br>SEO and traffic tips</p>
<div class="abs signup">
  <div class="abs signup-input">
    <svg width="13" height="11" viewBox="0 0 13 11" aria-hidden="true"><rect x="1" y="1" width="11" height="9" rx="1.5" fill="none" stroke="#a4a8ae"/><path d="M1.5 2 6.5 6 11.5 2" fill="none" stroke="#a4a8ae"/></svg>
    Enter your Email.
  </div>
  <div class="abs signup-btn">Send</div>
</div>

<!-- in the news -->
<div class="abs news-label">In the News</div>
<div class="abs news-mark" style="left:214px;width:96px" role="img" aria-label="Press outlet badge"></div>
<div class="abs news-mark" style="left:416px;width:145px" role="img" aria-label="Press outlet badge"></div>
<div class="abs news-mark" style="left:655px;width:114px" role="img" aria-label="Press outlet badge"></div>
<div class="abs news-mark" style="left:866px;width:145px" role="img" aria-label="Press outlet badge"></div>
<div class="abs divider" style="top:936px"></div>

<!-- testimonial one -->
<svg class="abs" style="left:255px;top:1005px" width="240" height="240" viewBox="0 0 240 240" role="img" aria-label="Portrait of Marla Quenby">
  <path d="M118 6C180 6 230 56 226 122C222 188 175 232 112 230C55 228 12 186 14 124C16 60 58 6 118 6Z" fill="#e4eef8"/>
  <circle cx="120" cy="118" r="94" fill="url(#g1)"/>
  <circle cx="55" cy="157" r="34" fill="#2a73bf" opacity=".55"/>
  <circle cx="36" cy="110" r="6" fill="#2a73bf" opacity=".7"/>
  <defs><linearGradient id="g1" x1="0" y1="0" x2="0" y2="1"><stop offset="0" stop-color="#d9d2c8"/><stop offset=".55" stop-color="#b68f7a"/><stop offset="1" stop-color="#1d2635"/></linearGradient></defs>
</svg>
<div class="abs quote-mark" style="left:485px;top:1018px">“</div>
<p class="abs quote-text" style="left:525px;top:1058px;width:400px">Elliot’s SEO knowledge is insane. If you want higher rankings, you neead to read his stuff – he’s the Unicorn among a sea of donkey SEOs.</p>
<div class="abs quote-by" style="left:525px;top:1168px"><strong>Marla Quenby</strong> &nbsp;·&nbsp; Author of Rivet Lane Marketing</div>

<!-- testimonial two -->
<p class="abs quote-text" style="left:271px;top:1320px;width:400px;text-align:right">Elliot’s SEO knowledge is insane. If you want higher rankings, you neead to read his stuff – he’s the Unicorn among a sea of donkey SEOs.</p>
<div class="abs quote-by" style="left:400px;top:1430px;width:271px;text-align:right"><strong>Tobin Vasquell</strong> &nbsp;·&nbsp; ClickHarbor</div>
<div class="abs quote-mark" style="left:689px;top:1280px">“</div>
<svg class="abs" style="left:712px;top:1266px" width="240" height="240" viewBox="0 0 240 240" role="img" aria-label="Portrait of Tobin Vasquell">
  <path d="M120 8C180 8 222 50 224 116C226 182 180 232 116 230C56 228 10 184 12 120C14 56 62 8 120 8Z" fill="#eef1f6"/>
  <circle cx="114" cy="117" r="96" fill="url(#g2)"/>
  <circle cx="170" cy="182" r="34" fill="#2a73bf" opacity=".55"/>
  <circle cx="209" cy="149" r="7" fill="#2a73bf" opacity=".7"/>
  <defs><linearGradient id="g2" x1="0" y1="0" x2="0" y2="1"><stop offset="0" stop-color="#c9c2b3"/><stop offset=".5" stop-color="#d8b89c"/><stop offset="1" stop-color="#1b2232"/></linearGradient></defs>
</svg>

<!-- case study -->
<div class="abs case"></div>
<h2 class="abs case-title">How I Increased<br>My Traffic By 110% In 14 Days</h2>
<div class="abs author"><div class="author-pic" role="img" aria-label="Avatar of Elliot Varnum"></div><span>Elliot Varnum, July 24th, 2019</span></div>

<h3 class="abs sub-head" style="top:1839px">Here’s the brutal truth about SEO:</h3>
<p class="abs body-copy" style="top:1884px">Lorem Ipsum is simply dummy text of the printing and typesetting industry. Lorem Ipsum has been the industry's standard dummy text ever since the 1500s, when an unknown printer took a galley of type and scrambled it to make a type specimen book. It has survived not only five centuries, but also the leap into electronic typesetting, remaining essentially unchanged. It was popularised in the 1960s with the release of Veltrace sheets containing Lorem Ipsum passages, and more recently with desktop publishing software like Orvane PageSmith including versions of Lorem Ipsum.</p>
<p class="abs body-copy" style="top:2039px">Sed ut perspiciatis unde omnis iste natus error sit voluptatem accusantium doloremque laudantium, totam rem aperiam, eaque ipsa quae ab illo inventore veritatis et quasi architecto beatae vitae dicta sunt explicabo. Nemo enim ipsam voluptatem quia voluptas sit aspernatur aut odit aut fugit, sed quia consequuntur magni dolores eos qui ratione voluptatem sequi nesciunt.</p>

<div class="abs chart-card" role="img" aria-label="Screenshot of a web analytics dashboard showing site visits rising steadily over the month"></div>

<h3 class="abs sub-head" style="top:2480px">The best part? It’s a simple, 3-step formula.</h3>
<p class="abs body-copy" style="top:2524px">Lorem Ipsum is simply dummy text of the printing and typesetting industry. Lorem Ipsum has been the industry's standard dummy text ever since the 1500s, when an unknown printer took a galley of type and scrambled it to make a type specimen book.</p>
<div class="abs cta">Click to Access The Case Study</div>

<!-- footer -->
<svg class="abs footer-bg" viewBox="0 0 1200 508" aria-hidden="true">
  <polygon points="0,199 1200,10 1200,508 0,508" fill="#0d57a7"/>
</svg>
<div class="abs" style="left:262px;top:2927px;width:46px;height:46px;border-radius:50%;background:var(--white)" role="img" aria-label="PawRank"></div>
<div class="abs foot-head" style="left:414px;top:2934px">PawRank</div>
<div class="abs foot-link" style="left:414px;top:2962px">Company</div>
<div class="abs foot-link" style="left:414px;top:2987px">Service</div>
<div class="abs foot-link" style="left:414px;top:3013px">Tools</div>
<div class="abs foot-link" style="left:414px;top:3038px">Blog</div>
<div class="abs foot-link" style="left:414px;top:3064px">Contact</div>
<div class="abs foot-head" style="left:639px;top:2934px">Quick Link</div>
<div class="abs foot-link" style="left:639px;top:2962px">Terms of Service</div>
<div class="abs foot-link" style="left:639px;top:2987px">Privacy</div>
<div class="abs social" style="left:914px;top:2938px" aria-label="Social profile"></div>
<div class="abs social" style="left:914px;top:2969px" aria-label="Social profile"></div>
<div class="abs social" style="left:914px;top:3000px" aria-label="Video channel"></div>
<div class="abs divider" style="top:3120px;background:rgba(255,255,255,.25)"></div>
<div class="abs copyright">© 2019 PawRank.</div>

</body>
</html>
```